Family business needs stationery redesign with new logo

Family owned company, established in 1987 wanting a brand 'refresh'. We are an electrical, refrigeration and construction company based in the Barkly Region Northern Territory, Australia. We have a new logo we would like to use which is uploaded along with our current letterhead and email signature. We are also dropping the word 'contractors' so please do not include this on any designs. Please note also, the 'orange' color used in our logo and designs should be Northern Territory red ochre which is as follows:

RGB (Hex): #C75B12
PantoneĀ® 159 C
CMYK: 1 / 74 / 100 / 7

We are needing our stationery redesigned using our new logo. Please include letterheads, business cards, envelopes, and email signatures.

We currently use our business letterheads for quotations, invoices, letters, HR matters, and internal memos.

We also need a separate simplified letterhead for internal paperwork such as employee leave forms, meeting agendas, and meeting minutes etc.
Updates

Reason: Needing more submissions of full package designs. We are wanting all our stationery, including business cards, letterheads, email signatures, envelopes, etc to be cohesive. We also require ALL the information, as supplied on our template letterhead, to be included on the new letterhead designs. including electrical license no.etc Thank you, K&M

Reason: needing more time as work has got in the way of looking over designs. A lot of designs not meeting the brief/criteria.

Industry/Entity Type

Business

Colors
0355a3
f37122

Requirements
Must have
• The 'orange' color used in the designs should be Northern Territory red ochre which is as follows:
• RGB (Hex): #C75B12
• PantoneĀ® 159 C
• CMYK: 1 / 74 / 100 / 7
• ***MUST INCLUDE ALL INFORMATION THAT IS ON OUR CURRENT LETTERHEAD***
Should not have
• Please do not include the word 'contractors'

```html
<!DOCTYPE html>
<html lang="en">
<head>
<meta charset="utf-8">
<title>K&amp;M Business Card</title>
<link href="https://fonts.googleapis.com/css2?family=Open+Sans:wght@400;600;700&display=swap" rel="stylesheet">
<style>
  :root {
    --navy: #1d386c;
    --ochre: #c75b12;
    --ink: #4a4a4a;
    --paper: #ffffff;
    --backdrop: #e6e9ea;
    --rule: #8a8f99;
  }
  * { box-sizing: border-box; margin: 0; padding: 0; }
  html, body { width: 1200px; height: 1200px; overflow: hidden; }
  body {
    background: var(--backdrop);
    font-family: "Open Sans", Arial, sans-serif;
    position: relative;
  }
  .card {
    position: absolute;
    left: 150px;
    width: 900px;
    height: 514px;
    overflow: hidden;
    box-shadow: 0 10px 30px rgba(0,0,0,0.12);
  }
  .card--front { top: 70px; background: var(--paper); }
  .card--back { top: 616px; background: var(--navy); }

  .card__swoosh { position: absolute; inset: 0; width: 100%; height: 100%; }

  .brand {
    position: absolute;
    display: flex;
    align-items: center;
    gap: 18px;
    font-weight: 700;
    letter-spacing: 2px;
    line-height: 1;
  }
  .brand__dot { border-radius: 50%; background: var(--ochre); }
  .card--front .brand { left: 330px; top: 48px; font-size: 90px; color: var(--navy); }
  .card--front .brand__dot { width: 24px; height: 24px; }
  .card--back .brand { left: 50%; top: 50%; transform: translate(-50%, -50%); font-size: 150px; color: var(--paper); }
  .card--back .brand__dot { width: 40px; height: 40px; }

  .person { position: absolute; left: 70px; top: 270px; }
  .person__name { font-size: 30px; font-weight: 700; color: var(--navy); line-height: 1.1; }
  .person__role { font-size: 24px; color: var(--ochre); margin-top: 2px; }
  .person__address { font-size: 20px; color: var(--ink); margin-top: 22px; line-height: 1.5; }

  .divider {
    position: absolute;
    left: 490px; top: 190px;
    width: 1px; height: 186px;
    background: var(--rule);
  }
  .contacts {
    position: absolute;
    left: 510px; top: 186px;
    list-style: none;
  }
  .contacts__item {
    display: flex;
    align-items: center;
    gap: 14px;
    font-size: 20px;
    color: var(--ink);
    height: 38px;
  }
  .contacts__icon { width: 24px; height: 24px; flex: none; }
</style>
</head>
<body>

<section class="card card--front" aria-label="Business card front">
  <svg class="card__swoosh" viewBox="0 0 900 514" preserveAspectRatio="none" aria-hidden="true">
    <path d="M0 514 L0 506 Q560 486 900 408 L900 514 Z" fill="var(--navy)"/>
    <path d="M0 498 Q560 478 900 398" fill="none" stroke="var(--ochre)" stroke-width="5"/>
  </svg>

  <div class="brand"><span class="brand__name">K&amp;M</span><span class="brand__dot"></span></div>

  <div class="person">
    <p class="person__name">Dana</p>
    <p class="person__role">Corporate Service Manager</p>
    <p class="person__address">42 Ridgeway St, Mulga Creek<br>NT 0870, Australia</p>
  </div>

  <div class="divider"></div>

  <ul class="contacts">
    <li class="contacts__item">
      <svg class="contacts__icon" viewBox="0 0 24 24" aria-hidden="true"><path d="M6 3 L9 3 L10 8 L8 9.5 Q10 14 14.5 16 L16 14 L21 15 L21 18 Q21 21 18 21 Q4 19 3 6 Q3 3 6 3 Z" fill="none" stroke="var(--navy)" stroke-width="1.8"/></svg>
      <span>08 8900 1234</span>
    </li>
    <li class="contacts__item">
      <svg class="contacts__icon" viewBox="0 0 24 24" aria-hidden="true"><rect x="7" y="2" width="10" height="20" rx="2" fill="none" stroke="var(--navy)" stroke-width="1.8"/><line x1="10.5" y1="18.5" x2="13.5" y2="18.5" stroke="var(--navy)" stroke-width="1.8"/></svg>
      <span>0400 555 210</span>
    </li>
    <li class="contacts__item">
      <svg class="contacts__icon" viewBox="0 0 24 24" aria-hidden="true"><rect x="6" y="3" width="12" height="6" fill="var(--navy)"/><rect x="3" y="9" width="18" height="9" rx="2" fill="var(--navy)"/><rect x="7" y="15" width="10" height="6" fill="var(--paper)" stroke="var(--navy)" stroke-width="1.6"/></svg>
      <span>08 8900 1235</span>
    </li>
    <li class="contacts__item">
      <svg class="contacts__icon" viewBox="0 0 24 24" aria-hidden="true"><rect x="2" y="5" width="20" height="14" fill="var(--navy)"/><path d="M2 5 L12 13 L22 5" fill="none" stroke="var(--paper)" stroke-width="1.6"/></svg>
      <span>service@kmservices.com.au</span>
    </li>
    <li class="contacts__item">
      <svg class="contacts__icon" viewBox="0 0 24 24" aria-hidden="true"><circle cx="12" cy="12" r="9" fill="var(--navy)"/><path d="M3 12 H21 M12 3 Q7 12 12 21 M12 3 Q17 12 12 21" fill="none" stroke="var(--paper)" stroke-width="1.3"/></svg>
      <span>www.kmservices.com.au</span>
    </li>
  </ul>
</section>

<section class="card card--back" aria-label="Business card back">
  <div class="brand"><span class="brand__name">K&amp;M</span><span class="brand__dot"></span></div>
</section>

</body>
</html>
```